Skincare Cleanser Bottle Label

New product launch of a mint facial cleanser.
Brand is called Dorvelle.
Product will be called Lunara.
Looking for a label design that can be printed using silk screening.
High gloss white plastic bottle. 8oz. White push pump top.
Clinical skincare brand, professional image, sold in medical spas.

Target Market(s)

Women Age 20-65

Industry/Entity Type

Health And Wellness

Font styles to use
Serif
Sans Serif

Requirements
Must have
• Dorvelle brand name in the orignal font.
Should not have
• Multiple colours.

```html
<!DOCTYPE html>
<html lang="en">
<head>
<meta charset="utf-8">
<title>Dorvelle Lunara – Mint Facial Cleanser Label</title>
<link rel="stylesheet" href="https://fonts.googleapis.com/css2?family=Montserrat:wght@400;500;700&display=swap">
<style>
  :root {
    --backdrop: #0d0d0d;
    --label-white: #ffffff;
    --ink: #111111;
    --ink-soft: #2a2a2a;
  }
  * { margin: 0; padding: 0; box-sizing: border-box; }
  html, body {
    width: 828px;
    height: 1200px;
    overflow: hidden;
    background: var(--backdrop);
  }
  .canvas {
    position: relative;
    width: 828px;
    height: 1200px;
    background: var(--backdrop);
  }
  .label {
    position: absolute;
    left: 210px;
    top: 60px;
    width: 408px;
    height: 1080px;
    background: var(--label-white);
    font-family: "Montserrat", sans-serif;
    color: var(--ink);
  }
  .product-band {
    position: absolute;
    left: 172px;
    right: 0;
    top: 16px;
    height: 74px;
    background: var(--ink);
    display: flex;
    align-items: center;
    padding-left: 14px;
  }
  .product-name {
    color: var(--label-white);
    font-weight: 500;
    font-size: 50px;
    letter-spacing: 1px;
    line-height: 1;
  }
  .product-type {
    position: absolute;
    right: 10px;
    top: 104px;
    font-weight: 400;
    font-size: 19px;
    letter-spacing: 0.2px;
    color: var(--ink-soft);
    white-space: nowrap;
  }
  .brand-name {
    position: absolute;
    left: 14px;
    top: 980px;
    transform-origin: left top;
    transform: rotate(-90deg);
    font-weight: 400;
    font-size: 54px;
    letter-spacing: 4px;
    line-height: 1;
    color: var(--ink);
    white-space: nowrap;
  }
  .volume {
    position: absolute;
    right: 22px;
    top: 1012px;
    font-weight: 500;
    font-size: 15px;
    letter-spacing: 0.5px;
    color: var(--ink-soft);
  }
</style>
</head>
<body>
  <main class="canvas">
    <section class="label">
      <div class="product-band">
        <h1 class="product-name">LUNARA</h1>
      </div>
      <p class="product-type">MINT FACIAL CLEANSER</p>
      <p class="brand-name">dorvelle</p>
      <p class="volume">8OZ.</p>
    </section>
  </main>
</body>
</html>
```